QuillMark Business Cards

I need a business card designed for QuillMark. To get an idea of what we do please visit https://formvault.example/para-creadores-3

```html
<!DOCTYPE html>
<html lang="en">
<head>
<meta charset="utf-8">
<title>QuillMark Business Cards</title>
<link rel="stylesheet" href="https://fonts.googleapis.com/css2?family=Montserrat:wght@400;500;600;700&family=Roboto:wght@400&display=swap">
<style>
  :root {
    --bg: #2a2b2e;
    --card: #17191c;
    --card-edge: #1f2226;
    --gold: #e8941f;
    --gold-edge: #c47a18;
    --white: #ffffff;
    --muted: #d9dadc;
    --rule: #8d8f93;
  }
  * { box-sizing: border-box; margin: 0; padding: 0; }
  html, body { width: 1200px; height: 963px; overflow: hidden; }
  body {
    background: var(--bg);
    display: flex;
    flex-direction: column;
    align-items: center;
    justify-content: center;
    gap: 56px;
    font-family: "Montserrat", sans-serif;
  }
  .card {
    position: relative;
    width: 700px;
    height: 400px;
    background: var(--card);
    border: 1px solid var(--card-edge);
    border-bottom: 4px solid var(--gold-edge);
    box-shadow: 0 10px 30px rgba(0,0,0,0.45);
    overflow: hidden;
  }

  /* Front */
  .front { display: flex; align-items: center; }
  .brand {
    width: 330px;
    padding-left: 60px;
    display: flex;
    flex-direction: column;
  }
  .brand-row { display: flex; align-items: center; gap: 16px; }
  .brand-square {
    width: 22px; height: 22px;
    background: var(--gold);
    flex: none;
  }
  .brand-name {
    font-weight: 700;
    font-size: 26px;
    letter-spacing: 3px;
    color: var(--white);
    text-transform: uppercase;
  }
  .brand-tagline {
    margin-top: 6px;
    margin-left: 38px;
    font-size: 8px;
    letter-spacing: 4px;
    color: var(--gold);
    text-transform: uppercase;
  }
  .brand-rule {
    margin-top: 6px;
    margin-left: 130px;
    width: 118px;
    height: 2px;
    background: var(--white);
  }
  .divider {
    width: 1px;
    height: 230px;
    background: var(--rule);
    margin-right: 38px;
  }
  .details { color: var(--muted); font-family: "Roboto", sans-serif; }
  .person-name {
    font-family: "Montserrat", sans-serif;
    font-weight: 700;
    font-size: 21px;
    color: var(--gold);
    text-transform: uppercase;
  }
  .person-role { font-size: 15px; margin-top: 4px; }
  .address { font-size: 15px; line-height: 1.3; margin-top: 22px; }
  .contact-list { list-style: none; margin-top: 22px; font-size: 15px; }
  .contact-list li { display: flex; align-items: center; gap: 12px; line-height: 1.7; }
  .contact-list svg { width: 15px; height: 15px; flex: none; }

  /* Back */
  .back {
    display: flex;
    align-items: center;
    justify-content: center;
  }
  .back-lockup { display: flex; flex-direction: column; }
  .back-name {
    font-weight: 500;
    font-size: 46px;
    letter-spacing: 16px;
    color: var(--white);
    text-transform: uppercase;
  }
  .back-tagline {
    margin-top: 8px;
    font-size: 12px;
    letter-spacing: 8px;
    color: var(--gold);
    text-transform: uppercase;
  }
  .back-rule {
    margin-top: 4px;
    margin-left: 250px;
    width: 200px;
    height: 1px;
    background: var(--white);
  }
</style>
</head>
<body>

  <section class="card front" aria-label="Card front">
    <div class="brand">
      <div class="brand-row">
        <span class="brand-square"></span>
        <span class="brand-name">QuillMark</span>
      </div>
      <span class="brand-tagline">Digital Notary</span>
      <span class="brand-rule"></span>
    </div>
    <div class="divider"></div>
    <div class="details">
      <h1 class="person-name">Daniel Reyes</h1>
      <p class="person-role">Manager</p>
      <p class="address">Your address, city<br>state, ZIP 0000</p>
      <ul class="contact-list">
        <li>
          <svg viewBox="0 0 16 16" fill="none" stroke="#e8941f" stroke-width="2" stroke-linecap="round"><path d="M4 2 Q1 8 6 13 Q9 15 11 13"/></svg>
          555-014-2100
        </li>
        <li>
          <svg viewBox="0 0 16 16" fill="none" stroke="#e8941f" stroke-width="1.4"><rect x="1.5" y="3.5" width="13" height="9"/><path d="M1.5 3.5 L8 9 L14.5 3.5"/></svg>
          hello@quillmark.example
        </li>
        <li>
          <svg viewBox="0 0 16 16" fill="none" stroke="#e8941f" stroke-width="1.3"><circle cx="8" cy="8" r="6.5"/><ellipse cx="8" cy="8" rx="3" ry="6.5"/><path d="M1.5 8 H14.5 M2.5 5 H13.5 M2.5 11 H13.5"/></svg>
          www.quillmark.example
        </li>
      </ul>
    </div>
  </section>

  <section class="card back" aria-label="Card back">
    <div class="back-lockup">
      <span class="back-name">QuillMark</span>
      <span class="back-tagline">Digital Notary</span>
      <span class="back-rule"></span>
    </div>
  </section>

</body>
</html>
```